Remodel Flyer for realtors

"K" Tandem Builders

4"x 9" rack card front and back

www.BrindleyRenovator.com

555-318-4762

Let us fix what your home inspector finds!

Send us your inspection summary.

We are a licensed and Insured contractor.
CRC4871093

Serving
Marion County and The Heronfield

This flyer will sit in realtor offices for realtors to give to there buyers and sellers.

Target Market(s)

Realtors

Industry/Entity Type

Construction

Colors

Designer to choose colors to be used in the design.

```html
<!DOCTYPE html>
<html lang="en">
<head>
<meta charset="utf-8">
<title>"K" Tandem Builders – Rack Card</title>
<link rel="stylesheet" href="https://fonts.googleapis.com/css2?family=Roboto+Condensed:wght@400;700&display=swap">
<style>
  :root {
    --canvas: #e6e7e9;
    --card: #ffffff;
    --ink: #4a4a4a;
    --ink-dark: #111111;
    --band: #58585a;
    --accent: #f2930c;
    --photo-room: linear-gradient(160deg, #e9e6e1 0%, #cfc8be 45%, #8d7a66 80%, #6b5848 100%);
    --photo-house: linear-gradient(180deg, #6f86a8 0%, #a08a86 45%, #8a4e3c 75%, #3e3a36 100%);
  }
  * { margin: 0; padding: 0; box-sizing: border-box; }
  html, body { width: 1200px; height: 800px; overflow: hidden; }
  body {
    background: var(--canvas);
    font-family: "Roboto Condensed", "Arial Narrow", sans-serif;
    color: var(--ink);
    position: relative;
  }
  .card {
    position: absolute;
    top: 21px;
    width: 311px;
    height: 699px;
    background: var(--card);
    overflow: hidden;
  }
  .card--front { left: 121px; }
  .card--back { left: 733px; }

  /* Front */
  .brand {
    position: absolute; left: 0; top: 0; width: 311px; height: 152px;
    display: flex; align-items: center; justify-content: center; gap: 10px;
  }
  .brand__mark { width: 22px; height: 22px; background: var(--accent); }
  .brand__name { font-size: 24px; font-weight: 700; color: var(--ink); letter-spacing: 1px; }
  .room-photo {
    position: absolute; left: 0; top: 152px; width: 311px; height: 376px;
    background: var(--photo-room);
  }
  .house-frame {
    position: absolute; left: 15px; top: 429px; width: 150px; height: 142px;
    background: #f1f0ee; padding: 9px 9px 0 9px;
  }
  .house-photo { width: 100%; height: 100%; background: var(--photo-house); }
  .serving {
    position: absolute; right: 18px; top: 546px;
    font-size: 28px; color: var(--accent); line-height: 1;
  }
  .serving-rule {
    position: absolute; left: 185px; top: 575px; width: 88px; height: 2px; background: var(--ink);
  }
  .area {
    position: absolute; left: 0; width: 311px; top: 581px;
    text-align: center; font-size: 21px; line-height: 1.2;
  }
  .front-band {
    position: absolute; left: 0; bottom: 0; width: 311px; height: 89px;
    background: var(--band); color: #fff; text-align: center;
  }
  .front-band__web { font-size: 25px; margin-top: 6px; line-height: 1.1; }
  .front-band__phone {
    display: flex; align-items: center; justify-content: center; gap: 14px;
    font-size: 36px; line-height: 1; margin-top: 8px;
  }

  /* Back */
  .before-after { position: absolute; left: 0; top: 0; }
  .tag {
    position: absolute; font-size: 21px; color: var(--ink-dark);
    background: rgba(255,255,255,0.8); padding: 0 5px; line-height: 26px;
  }
  .tag--before { left: 2px; top: 157px; }
  .tag--after { right: 0; top: 410px; width: 71px; }
  .headline {
    position: absolute; left: 15px; top: 426px;
    font-size: 33px; line-height: 37px; color: var(--ink);
  }
  .headline em { font-style: normal; color: var(--accent); }
  .request {
    position: absolute; left: 0; width: 311px; top: 550px;
    text-align: center; font-size: 21px; line-height: 21px; padding-left: 4px;
  }
  .request-rule {
    position: absolute; left: 65px; top: 600px; width: 158px; height: 2px; background: var(--ink);
  }
  .back-web {
    position: absolute; left: 0; width: 311px; top: 605px;
    text-align: center; font-size: 27px; color: var(--accent);
  }
  .back-band {
    position: absolute; left: 0; bottom: 0; width: 311px; height: 54px;
    background: var(--band); color: #fff; text-align: center;
    font-size: 16px; line-height: 21px; padding-top: 4px;
  }
  .back-band__license { font-size: 21px; }

  .side-label {
    position: absolute; top: 737px; width: 200px; text-align: center;
    font-size: 36px; color: var(--ink-dark); line-height: 1;
  }
  .side-label--front { left: 177px; }
  .side-label--back { left: 788px; }
</style>
</head>
<body>

<section class="card card--front">
  <div class="brand">
    <span class="brand__mark"></span>
    <span class="brand__name">"K" Tandem Builders</span>
  </div>
  <div class="room-photo" role="img" aria-label="Bright remodeled living room with a grey sectional sofa and wooden coffee table"></div>
  <div class="house-frame">
    <div class="house-photo" role="img" aria-label="Two-storey brick home exterior at dusk"></div>
  </div>
  <div class="serving">Serving</div>
  <div class="serving-rule"></div>
  <div class="area">Marion County and The Heronfield</div>
  <div class="front-band">
    <div class="front-band__web">www.BrindleyRenovator.com</div>
    <div class="front-band__phone">
      <svg width="32" height="32" viewBox="0 0 32 32" aria-hidden="true">
        <circle cx="16" cy="16" r="14" fill="none" stroke="#f2930c" stroke-width="2.5"/>
        <path d="M11 9 l3 -1 l2 4 l-2 2 q1.5 3 4 4 l2 -2 l4 2 l-1 3 q-1 1 -3 1 q-6 -1 -10 -8 q-1 -3 1 -5z" fill="#f2930c"/>
      </svg>
      <span>555-318-4762</span>
    </div>
  </div>
</section>

<section class="card card--back">
  <svg class="before-after" width="311" height="699" viewBox="0 0 311 699">
    <defs>
      <linearGradient id="before-tone" x1="0" y1="0" x2="1" y2="1">
        <stop offset="0" stop-color="#a89a86"/>
        <stop offset="0.5" stop-color="#c9b9a3"/>
        <stop offset="1" stop-color="#4f7066"/>
      </linearGradient>
      <linearGradient id="after-tone" x1="0" y1="0" x2="1" y2="1">
        <stop offset="0" stop-color="#eceae6"/>
        <stop offset="0.55" stop-color="#cfcac3"/>
        <stop offset="1" stop-color="#55585a"/>
      </linearGradient>
    </defs>
    <polygon role="img" aria-label="Dated kitchen before remodel with green countertops and red valances" points="0,0 311,0 311,91 0,217" fill="url(#before-tone)"/>
    <polygon role="img" aria-label="Remodeled white kitchen with grey quartz counters after renovation" points="0,223 311,97 311,471 0,366" fill="url(#after-tone)"/>
  </svg>
  <div class="tag tag--before">Before</div>
  <div class="tag tag--after">After</div>
  <h1 class="headline" style="font-weight:400">Let us<br>fix what your <em>home</em><br>inspector finds!</h1>
  <p class="request">Send us your<br>inspection summary.</p>
  <div class="request-rule"></div>
  <div class="back-web">www.BrindleyRenovator.com</div>
  <div class="back-band">
    <div>We are a licensed and Insured contractor.</div>
    <div class="back-band__license">CRC4871093</div>
  </div>
</section>

<div class="side-label side-label--front">Front</div>
<div class="side-label side-label--back">Back</div>

</body>
</html>
```